Business Card Design

Certified Canine Therapeutic Massage Practitioner
Specializing in Senior Canine Massage Therapy and Giant Breeds
Certified in Canine Emergency CPR, First Aid 7 Care

Target Market(s)

Dog lovers with disposable income.

Industry/Entity Type

Business

Contact Information for Business Card

Paws Unwound Studio
614.382.5097
Nashville, TN
Rulo@Pawsunwoundstudio.com

```html
<!DOCTYPE html>
<html lang="en">
<head>
<meta charset="utf-8">
<title>Paws Unwound Studio — Business Card</title>
<link href="https://fonts.googleapis.com/css2?family=Exo+2:wght@300;400&display=swap" rel="stylesheet">
<style>
  :root{
    --canvas:#e4e4e4;
    --forest-deep:#0f2414;
    --forest:#24472a;
    --forest-light:#3d6b3c;
    --band:#172d1b;
    --paper:#ffffff;
    --copper:#b9724f;
    --copper-fold:#7c4430;
    --ribbon-ink:#3a2619;
    --light-ink:#f4f1ec;
    --email-ink:#eadfd2;
    --mark:#6d4a3a;
    --illus-a:#efe1d6;
    --illus-b:#d8b9a4;
  }
  *{box-sizing:border-box;margin:0;padding:0}
  html,body{width:1190px;height:1200px;overflow:hidden;background:var(--canvas)}
  body{font-family:"Exo 2",sans-serif;font-weight:300;position:relative}

  .card{position:absolute;left:145px;width:900px;height:514px;overflow:hidden;
        box-shadow:0 10px 28px rgba(0,0,0,.18)}
  .card--front{top:50px}
  .card--back{top:636px;background:var(--paper)}

  /* front */
  .front-photo{position:absolute;inset:0;
    background:
      radial-gradient(ellipse 240px 260px at 170px 250px, rgba(190,200,205,.45), transparent 70%),
      radial-gradient(ellipse 230px 220px at 400px 330px, rgba(150,95,60,.55), transparent 70%),
      linear-gradient(135deg,var(--forest-light) 0%,var(--forest) 45%,var(--forest-deep) 100%)}
  .brand-title{position:absolute;right:60px;top:96px;text-align:right;color:var(--light-ink);
    font-weight:300;font-size:78px;line-height:.95;letter-spacing:1px;text-transform:uppercase}
  .front-band{position:absolute;left:0;right:0;bottom:0;height:78px;background:rgba(23,45,27,.88);
    display:flex;align-items:center;padding-left:88px;color:var(--light-ink);font-size:32px;letter-spacing:.5px}

  /* back */
  .ribbon{position:absolute;left:0;height:96px;background:var(--copper);color:var(--ribbon-ink);
    font-size:26px;line-height:1.15;padding:14px 0 0 34px}
  .ribbon::after{content:"";position:absolute;right:0;bottom:-14px;border-top:14px solid var(--copper-fold);
    border-right:24px solid transparent}
  .ribbon--1{top:20px;width:470px}
  .ribbon--2{top:140px;width:520px}
  .ribbon--3{top:260px;width:470px}

  .back-mark{position:absolute;left:560px;top:90px;width:300px;display:flex;align-items:center;gap:14px;
    color:var(--mark);font-size:36px;line-height:1;font-weight:400;text-transform:uppercase}
  .back-mark__dot{flex:none;width:26px;height:26px;border-radius:50%;background:var(--copper)}
  .dog-illustration{position:absolute;left:600px;top:250px;width:230px;height:180px;
    background:linear-gradient(160deg,var(--illus-a),var(--illus-b));border-radius:6px}
  .back-band{position:absolute;left:0;right:0;bottom:0;height:66px;background:var(--band)}
  .back-email{position:absolute;left:160px;bottom:12px;color:var(--email-ink);font-size:30px;letter-spacing:.5px}
</style>
</head>
<body>

<section class="card card--front">
  <div class="front-photo" role="img" aria-label="Photo of the massage practitioner seated beside a large Saint Bernard in front of green woodland"></div>
  <h1 class="brand-title">Paws<br>Unwound<br>Studio</h1>
  <div class="front-band">614.382.5097 | Nashville, TN</div>
</section>

<section class="card card--back">
  <div class="ribbon ribbon--1">Certified Canine Therapeutic<br>Massage Practitioner</div>
  <div class="ribbon ribbon--2">Specializing in Senior Canine<br>Massage Therapy and Giant Breeds</div>
  <div class="ribbon ribbon--3">Certified in Canine Emergency<br>CPR, First Aid &amp; Care</div>

  <div class="back-mark"><span class="back-mark__dot"></span><span>Paws Unwound Studio</span></div>
  <div class="dog-illustration" role="img" aria-label="Line illustration of two standing dogs in soft tan tones"></div>

  <div class="back-band"></div>
  <div class="back-email">Rulo@Pawsunwoundstudio.com</div>
</section>

</body>
</html>
```